DESIGN FOR TRADE SHOW FLOOR DISPLAY

March 25: I FORGOT TO INCLUDE THE OUTLINE OF WHAT I WANT FOR THE BOOTH. I JUST ADDED IT HERE. The document is called BOOTH DESIGN.

I need a design for a booth for trade shows. To see what I mean, please look at image 1 attached below.

The back wall part of the display shows graphics on the front of the display as well as the sides of the display.

I also need to have a design for the podium. See image 1 below.

I've attached the specifications for the designs.

The document for the back wall is called GRAPHIC TEMPLATE DESIGN FOR BACK WALL.

The document for the podium is called PODIUM TEMPLATE.

I've attached two other documents:

1. A large image of the cover of my book.

2. A copy of the Wrenfield Capital logo.

I think this is everything that you will need. Please let me know if there is anything else that you need.

Thanks!

Ned Calloway

Target Market(s)

CPAs and accountants. Financial professionals.

Industry/Entity Type

Trade

Font styles to use
Other font styles liked:
• Use your best idea to worth with book cover and logo.

Requirements
Must have
• The colors and fonts work well with both the book cover and the Wrenfield Capital logo.
• I've attached samples of booth designs that I like. They are called Sample 1, Sample 2, Sample 3, Sample 4. They are in no particular order.

```html
<!DOCTYPE html>
<html lang="en">
<head>
<meta charset="utf-8">
<title>Trade Show Booth – Back Wall and Podium Graphics</title>
<link href="https://fonts.googleapis.com/css2?family=Bebas+Neue&family=Oswald:wght@400;500&family=Cinzel:wght@400;600&display=swap" rel="stylesheet">
<style>
  :root {
    --stage: #e4e5e8;
    --blue: #1f8fd2;
    --blue-light: #3aa7e2;
    --blue-deep: #0b5e9e;
    --cyan: #2bb8d8;
    --ink: #0d0f12;
    --title-grey: #dfe3e6;
    --white: #ffffff;
    --rule: #cfe6f4;
    --logo-green: #3a9a4a;
  }
  * { box-sizing: border-box; margin: 0; padding: 0; }
  html, body { width: 1200px; height: 880px; overflow: hidden; }
  body { background: var(--stage); position: relative; font-family: "Oswald", sans-serif; }

  /* ---------- Back wall ---------- */
  .back-wall { position: absolute; left: 34px; top: 110px; width: 860px; height: 640px; display: flex; }
  .wall-side { width: 44px; height: 100%; background: var(--ink); display: flex; flex-direction: column; }
  .wall-side .cap { height: 38px; background: var(--blue); border-bottom: 3px solid var(--white); }
  .wall-side .cap.bottom { height: 30px; border-bottom: 0; border-top: 3px solid var(--white); margin-top: auto; }
  .side-text { flex: 1; display: flex; align-items: center; justify-content: flex-start; padding: 40px 0; gap: 44px; writing-mode: vertical-rl; font-family: "Oswald", sans-serif; font-weight: 500; font-size: 17px; letter-spacing: 1px; color: var(--white); white-space: nowrap; }
  .side-text .accent { color: var(--cyan); }
  .side-text .author { font-family: "Cinzel", serif; font-weight: 400; font-size: 15px; letter-spacing: 3px; }
  .wall-side.left .side-text { transform: rotate(180deg); }

  .wall-front { width: 772px; height: 100%; display: flex; flex-direction: column; background: var(--blue); }
  .front-top { height: 38px; background: linear-gradient(var(--blue-light), var(--blue)); border-bottom: 4px solid var(--rule); }
  .front-body { flex: 1; display: flex; }
  .front-bottom { height: 30px; background: var(--blue); border-top: 4px solid var(--rule); }

  /* book cover column */
  .cover { width: 388px; display: flex; flex-direction: column; background: var(--ink); }
  .cover-art { position: relative; flex: 1; }
  .author-photo { position: absolute; inset: 0; background: linear-gradient(100deg, #2b2f36 0%, #56504a 30%, #3b4049 55%, #16324c 80%, #0e2a45 100%); }
  .book-title { position: absolute; right: 14px; top: 60px; text-align: right; font-family: "Bebas Neue", sans-serif; font-weight: 400; font-size: 74px; line-height: 0.92; color: var(--title-grey); }
  .book-title .accent { color: var(--cyan); }
  .cover-subtitle { height: 70px; background: var(--blue); border-top: 3px solid var(--white); border-bottom: 3px solid var(--white); display: flex; align-items: center; justify-content: center; text-align: center; font-family: "Cinzel", serif; font-size: 18px; line-height: 1.1; color: var(--white); }
  .cover-author { height: 62px; display: flex; align-items: center; justify-content: center; font-family: "Cinzel", serif; font-size: 26px; letter-spacing: 8px; color: var(--white); }

  /* alliance column */
  .alliance { flex: 1; display: flex; flex-direction: column; background: linear-gradient(180deg, var(--blue) 0%, #1676bb 55%, var(--blue) 100%); border-left: 3px solid var(--white); }
  .alliance-heading { margin-top: 66px; text-align: center; font-family: "Oswald", sans-serif; font-weight: 400; font-size: 25px; line-height: 1.3; color: var(--white); letter-spacing: 0.5px; }
  .benefits { list-style: none; margin: 34px 0 0 46px; }
  .benefits li { display: flex; align-items: center; gap: 14px; font-size: 20px; color: var(--white); height: 46px; letter-spacing: 0.3px; }
  .benefits li::before { content: ""; width: 10px; height: 10px; background: radial-gradient(circle, #9fd6f2 1.2px, transparent 1.6px) 0 0 / 5px 5px; }
  .partner-band { margin-top: auto; margin-bottom: 62px; height: 70px; background: var(--white); display: flex; align-items: center; padding-left: 40px; gap: 12px; }
  .partner-band .mark { width: 26px; height: 26px; background: var(--logo-green); }
  .partner-band .name { font-family: "Oswald", sans-serif; font-weight: 500; font-size: 22px; color: var(--blue-deep); }

  /* ---------- Podium ---------- */
  .podium { position: absolute; left: 920px; top: 420px; width: 250px; height: 330px; display: flex; }
  .podium-side { width: 26px; background: var(--ink); display: flex; align-items: center; justify-content: center; }
  .podium-side span { writing-mode: vertical-rl; font-family: "Oswald", sans-serif; font-size: 10px; color: var(--white); letter-spacing: 1px; white-space: nowrap; }
  .podium-front { flex: 1; background: radial-gradient(ellipse at 50% 30%, var(--blue-light), var(--blue) 60%, var(--blue-deep)); border-top: 4px solid var(--rule); display: flex; align-items: center; justify-content: center; }
  .mini-cover { width: 128px; height: 194px; background: var(--ink); display: flex; flex-direction: column; }
  .mini-art { position: relative; flex: 1; }
  .mini-art .author-photo { background: linear-gradient(100deg, #2b2f36 0%, #56504a 35%, #1a3a58 80%); }
  .mini-art .book-title { right: 6px; top: 10px; font-size: 25px; }
  .mini-cover .cover-subtitle { height: 28px; font-size: 7px; border-width: 1px; }
  .mini-cover .cover-author { height: 22px; font-size: 10px; letter-spacing: 3px; }
</style>
</head>
<body>
  <section class="back-wall">
    <div class="wall-side left">
      <div class="cap"></div>
      <div class="side-text"><span class="author">NED CALLOWAY</span><span>BUILD WEALTH THE <span class="accent">SMART WAY</span></span></div>
      <div class="cap bottom"></div>
    </div>

    <div class="wall-front">
      <div class="front-top"></div>
      <div class="front-body">
        <div class="cover">
          <div class="cover-art">
            <div class="author-photo" role="img" aria-label="Portrait photograph of the author in a dark suit and light tie"></div>
            <h1 class="book-title">BUILD<br>WEALTH<br>THE<br><span class="accent">SMART<br>WAY</span></h1>
          </div>
          <p class="cover-subtitle">A Plain Guide to Lasting<br>Investment Success</p>
          <p class="cover-author">NED CALLOWAY</p>
        </div>

        <div class="alliance">
          <h2 class="alliance-heading">JOIN OUR<br>STRATEGIC ALLIANCE PROGRAM</h2>
          <ul class="benefits">
            <li>OFFER FINANCIAL PLANNING SERVICES</li>
            <li>INCREASE CLIENT RETENTION</li>
            <li>STRENGTHEN CLIENT RELATIONSHIPS</li>
            <li>INCREASE CLIENT REFERRALS</li>
            <li>ENHANCE YOUR REPUTATION</li>
            <li>EARN ONGOING REVENUE</li>
          </ul>
          <div class="partner-band">
            <span class="mark"></span>
            <span class="name">Wrenfield Capital</span>
          </div>
        </div>
      </div>
      <div class="front-bottom"></div>
    </div>

    <div class="wall-side right">
      <div class="cap"></div>
      <div class="side-text"><span>BUILD WEALTH THE <span class="accent">SMART WAY</span></span><span class="author">NED CALLOWAY</span></div>
      <div class="cap bottom"></div>
    </div>
  </section>

  <section class="podium">
    <div class="podium-side"><span>BUILD WEALTH THE SMART WAY</span></div>
    <div class="podium-front">
      <div class="mini-cover">
        <div class="mini-art">
          <div class="author-photo" role="img" aria-label="Portrait photograph of the author in a dark suit"></div>
          <p class="book-title">BUILD<br>WEALTH<br>THE<br><span class="accent">SMART<br>WAY</span></p>
        </div>
        <p class="cover-subtitle">A Plain Guide to Lasting<br>Investment Success</p>
        <p class="cover-author">NED CALLOWAY</p>
      </div>
    </div>
  </section>
</body>
</html>
```